Epoxy Flooring Contractor business card

We need a business card to promote a new addition to our business. We now offer Epoxy Flooring. We would like for the business card to include the images attached. One is our logo, the other is a sample of metallic epoxy flooring, we would like to incorporate that somewhere into the design. I was thinking an icon of a man pushing a concrete grinder and have the color set to the metallic epoxy color. I found a business card sample on this website, I will attach it. It has the icon that we are looking for, or something similar.
Our company name is Harborline Coatings LLC
Our owners name is Dane Morrow
Phone is 561-482-7160
website is www.harborline-coatingsllc.example
please let me know if you need any other info

Contact Information for Business Card

Harborline Coatings LLC
Dane Morrow, owner
Phone: 561-482-7160
Address: P.O Box 8241 Lake Worth, FL 33467
www.Harborline-CoatingsLLC.example
HarborlineCoatingsLLC@mailbox.example
Include logo attached
It must include a Clip art of man with concrete grinder
Must include metallic epoxy design attached
Must include the following text
Residential Garage Flooring
Epoxy Countertops
Commercial Epoxy Flooring
Restaurant Flooring
Warehouse Flooring
Licensed & Insured
Free Estimates

Colors

Designer to choose colors to be used in the design.

Requirements
Must have
• Include logo attached
• It must include a Clip art of man with concrete grinder
• Must include metallic epoxy design attached
• Must include the following text
• Garage Epoxy Flooring
• Residential Epoxy Flooring
• Concrete Floor Crack Repairs
• Concrete Floor Grinding
• Commercial & Warehouse Epoxy Flooring
• Restaurant Epoxy Flooring
• Epoxy Countertops
• Non Slip Epoxy Pool Decks
• Textured Finishes, Flakes, Granite Coat, Metallic & Quartz
• FREE ESTIMATES • LICENSED & INSURED

```html
<!DOCTYPE html>
<html lang="en">
<head>
<meta charset="utf-8">
<title>Harborline Coatings – Business Card</title>
<link href="https://fonts.googleapis.com/css2?family=Montserrat:wght@500&family=Open+Sans:wght@400;700;800&display=swap" rel="stylesheet">
<style>
  :root {
    --brand-blue: #4a6f98;
    --light-blue: #7ea9d6;
    --logo-gray: #6e6e6e;
    --ink: #333a40;
    --card-white: #ffffff;
    --backdrop: #2a2b2d;
    --band-blue: rgba(74, 111, 152, 0.74);
  }
  * { box-sizing: border-box; margin: 0; padding: 0; }
  html, body {
    width: 1200px; height: 1200px; overflow: hidden;
    background: var(--backdrop);
    font-family: "Open Sans", sans-serif;
  }
  .card {
    position: absolute; left: 120px; width: 960px; height: 548px;
    background: var(--card-white); overflow: hidden;
    box-shadow: 0 10px 30px rgba(0,0,0,.45);
  }
  .card--front { top: 40px; }
  .card--back { top: 612px; }
  .abs { position: absolute; }

  /* Front */
  .finish-samples { left: 0; top: 0; width: 700px; height: 228px; display: flex; }
  .finish-sample { flex: 1; }
  .finish-sample--silver { background: radial-gradient(circle at 40% 50%, #b5b5b2, #8a8a86); }
  .finish-sample--flake { background: linear-gradient(135deg, #c9ccd2, #8d939b 55%, #d8dbe0); }
  .finish-sample--blue { background: radial-gradient(circle at 50% 45%, #5b8fcf, #2a5ea3); }
  .rule { left: 0; width: 100%; background: var(--brand-blue); }
  .front-rule-top { top: 228px; height: 10px; }
  .front-rule-mid { top: 410px; height: 8px; }
  .grinder-art {
    left: 742px; top: 24px; width: 168px; height: 196px; border-radius: 6px;
    background: linear-gradient(160deg, #9dbbdc, var(--brand-blue));
  }

  .brand { display: flex; align-items: center; gap: 18px; }
  .brand-square { width: 64px; height: 64px; background: var(--brand-blue); flex: none; }
  .brand-name {
    font-family: "Montserrat", sans-serif; font-weight: 500;
    color: var(--logo-gray); font-size: 42px; line-height: 1.05; letter-spacing: 3px;
  }
  .card--front .brand { left: 90px; top: 272px; }

  .contact-list { left: 540px; top: 296px; list-style: none; }
  .contact-item {
    display: flex; align-items: center; gap: 12px;
    font-size: 17px; color: var(--ink); line-height: 30px;
  }
  .contact-icon { width: 18px; height: 18px; flex: none; }

  .owner { left: 90px; top: 428px; }
  .owner-name { font-size: 30px; font-weight: 800; color: var(--brand-blue); line-height: 1.1; letter-spacing: 1px; }
  .owner-role { font-size: 14px; color: var(--ink); line-height: 1.2; }
  .owner-company { font-size: 18px; color: var(--light-blue); line-height: 1.3; }
  .owner-address { font-size: 18px; color: var(--ink); line-height: 1.3; }

  /* Back */
  .site-photo {
    left: 0; top: 0; width: 100%; height: 330px;
    background: linear-gradient(180deg, #8f9498 0%, #b9bcbf 45%, #e4e6e8 100%);
  }
  .service-band {
    left: 0; top: 58px; width: 100%; padding: 28px 36px;
    background: var(--band-blue);
    color: #fff; font-weight: 700; font-size: 19px; line-height: 1.45;
  }
  .back-rule-top { top: 330px; height: 12px; }
  .back-base {
    left: 0; top: 342px; width: 100%; height: 160px;
    background: linear-gradient(180deg, #f3f4f6, #e2e4e7);
  }
  .card--back .brand { left: 90px; top: 374px; }
  .back-phone {
    right: 60px; top: 356px; font-size: 46px; font-weight: 400; color: var(--brand-blue);
  }
  .social-row { right: 64px; top: 428px; display: flex; gap: 12px; }
  .social-dot { width: 34px; height: 34px; border-radius: 50%; background: var(--brand-blue); }
  .back-rule-bottom { top: 502px; height: 10px; }
  .flake-strip {
    left: 0; top: 512px; width: 100%; height: 36px;
    background: linear-gradient(90deg, #9a9ea3, #d6d8db 50%, #8e9297);
  }
</style>
</head>
<body>

<section class="card card--front">
  <div class="finish-samples abs">
    <div class="finish-sample finish-sample--silver" role="img" aria-label="Silver metallic epoxy floor sample"></div>
    <div class="finish-sample finish-sample--flake" role="img" aria-label="Gray, black and blue flake epoxy floor sample"></div>
    <div class="finish-sample finish-sample--blue" role="img" aria-label="Blue metallic epoxy floor sample"></div>
  </div>
  <div class="rule front-rule-top abs"></div>
  <div class="grinder-art abs" role="img" aria-label="Clip art of a worker pushing a concrete grinder"></div>

  <div class="brand abs">
    <div class="brand-square"></div>
    <div class="brand-name">Harborline<br>Coatings</div>
  </div>

  <ul class="contact-list abs">
    <li class="contact-item">
      <svg class="contact-icon" viewBox="0 0 24 24"><path fill="#4a6f98" d="M6.6 10.8a15 15 0 0 0 6.6 6.6l2.2-2.2a1 1 0 0 1 1-.25 11.4 11.4 0 0 0 3.6.57 1 1 0 0 1 1 1V20a1 1 0 0 1-1 1A17 17 0 0 1 3 4a1 1 0 0 1 1-1h3.5a1 1 0 0 1 1 1c0 1.25.2 2.45.57 3.57a1 1 0 0 1-.25 1z"/></svg>
      561-482-7160
    </li>
    <li class="contact-item">
      <svg class="contact-icon" viewBox="0 0 24 24"><rect x="2" y="5" width="20" height="14" rx="1.5" fill="#4a6f98"/><path d="M3 6l9 7 9-7" fill="none" stroke="#fff" stroke-width="1.6"/></svg>
      HarborlineCoatingsLLC@mailbox.example
    </li>
    <li class="contact-item">
      <svg class="contact-icon" viewBox="0 0 24 24"><g fill="none" stroke="#4a6f98" stroke-width="1.6"><circle cx="12" cy="12" r="9"/><ellipse cx="12" cy="12" rx="4" ry="9"/><path d="M3 12h18M5 7h14M5 17h14"/></g></svg>
      www.harborline-coatingsllc.example
    </li>
  </ul>

  <div class="rule front-rule-mid abs"></div>

  <div class="owner abs">
    <p class="owner-name">DANE MORROW</p>
    <p class="owner-role">owner</p>
    <p class="owner-company">Harborline Coatings LLC</p>
    <p class="owner-address">P.O Box 8241 Lake Worth, FL 33467</p>
  </div>
</section>

<section class="card card--back">
  <div class="site-photo abs" role="img" aria-label="Photo of a warehouse interior with a glossy epoxy-coated floor"></div>
  <p class="service-band abs">
    Garage Epoxy Flooring, Residential Epoxy Flooring, Concrete Floor Crack Repairs,<br>
    Concrete Floor Grinding, Commercial &amp; Warehouse Epoxy Flooring, Restaurant<br>
    Epoxy Flooring, Epoxy Countertops, Non Slip Epoxy Pool Decks, Textured Finishes,<br>
    Flakes, Granite Coat, Metallic &amp; Quartz, FREE ESTIMATES, LICENSED &amp; INSURED.
  </p>
  <div class="rule back-rule-top abs"></div>
  <div class="back-base abs" role="img" aria-label="Light gray flake epoxy texture"></div>

  <div class="brand abs">
    <div class="brand-square"></div>
    <div class="brand-name">Harborline<br>Coatings</div>
  </div>

  <p class="back-phone abs">561-482-7160</p>
  <div class="social-row abs">
    <span class="social-dot"></span>
    <span class="social-dot"></span>
  </div>

  <div class="rule back-rule-bottom abs"></div>
  <div class="flake-strip abs" role="img" aria-label="Black and white flake epoxy texture strip"></div>
</section>

</body>
</html>
```